I need a business card/logo designed that obviously describes my business. We are a residential appraisal and home inspection company in Springfield, MO. We offer residential appraisals, home inspection, pest inspection and radon gas measurement. We have been in business for 18 years and hold state certified residential appraisal licenses and DRUMI certified home inspection licenses. I have a logo that I really like and will attach, but would be open to new suggestions. I like more modern designs than traditional and would like a two sided card with our services, licenses and qualifications on the back.

```html
<!DOCTYPE html>
<html lang="en">
<head>
<meta charset="utf-8">
<title>Larkvale Dwelling Review – Business Card</title>
<link href="https://fonts.googleapis.com/css2?family=Josefin+Sans:wght@400;600;700&display=swap" rel="stylesheet">
<style>
  :root {
    --orange: #ef9a2a;
    --charcoal: #3a3a3a;
    --charcoal-dark: #262626;
    --paper: #ffffff;
    --ink: #2b2b2b;
    --muted: #cfcfcf;
    --stage: #e9e7e3;
    --brand: #d9862a;
  }
  * { box-sizing: border-box; margin: 0; padding: 0; }
  html, body {
    width: 1200px; height: 800px; overflow: hidden;
    background: var(--stage);
    font-family: "Josefin Sans", "Century Gothic", sans-serif;
  }
  .stage {
    position: relative; width: 1200px; height: 800px;
    display: flex; align-items: center; justify-content: center; gap: 40px;
  }
  .card {
    position: relative; width: 540px; height: 310px; overflow: hidden;
    border-radius: 4px;
    box-shadow: 0 10px 28px rgba(0,0,0,.22);
  }

  /* ---------- front ---------- */
  .card-front { background: var(--paper); }
  .name-band {
    position: absolute; left: 0; top: 0; width: 335px; height: 58px;
    background: var(--orange);
    border-bottom-right-radius: 18px;
    padding: 12px 0 0 46px; color: var(--paper);
  }
  .person-name { font-size: 19px; font-weight: 600; letter-spacing: 1px; }
  .person-role { font-size: 13px; margin-top: 2px; }
  .contact-panel {
    position: absolute; left: 0; top: 58px; width: 345px; height: 140px;
    background: linear-gradient(180deg, var(--charcoal) 0%, var(--charcoal-dark) 100%);
    border-bottom-right-radius: 18px;
    color: #f1f1f1; font-size: 12.5px; line-height: 1.25;
    padding: 14px 0 0 46px;
  }
  .contact-row { display: flex; gap: 12px; align-items: flex-start; margin-bottom: 9px; }
  .contact-row.divided { border-bottom: 1px solid #6a6a6a; padding-bottom: 8px; width: 250px; }
  .contact-icon { width: 13px; height: 13px; flex: none; margin-top: 1px; fill: #f1f1f1; }
  .web-footer {
    position: absolute; left: 70px; top: 258px;
    font-size: 13px; font-weight: 700; letter-spacing: 2.5px; color: var(--ink);
  }
  .accent-band {
    position: absolute; right: 0; top: 208px; width: 205px; height: 52px;
    background: var(--orange);
    border-top-left-radius: 16px;
  }
  .accent-base {
    position: absolute; right: 0; top: 260px; width: 205px; height: 50px;
    background: var(--charcoal-dark);
  }
  .brand {
    color: var(--brand); font-weight: 700; line-height: 1.1;
    display: flex; align-items: center; gap: 10px; white-space: nowrap;
  }
  .brand-mark { width: 13px; height: 13px; background: var(--brand); flex: none; }
  .card-front .brand {
    position: absolute; left: 362px; top: 88px; font-size: 19px;
  }

  /* ---------- back ---------- */
  .card-back {
    background: linear-gradient(160deg, #4a4a4a 0%, var(--charcoal-dark) 60%, #1c1c1c 100%);
    color: var(--paper);
  }
  .brand-plate {
    position: absolute; left: 210px; right: 0; top: 34px; height: 84px;
    background: var(--paper);
    border-top-left-radius: 14px; border-bottom-left-radius: 14px;
    display: flex; align-items: center; justify-content: center;
  }
  .card-back .brand { font-size: 21px; }
  .back-details {
    position: absolute; left: 36px; right: 36px; top: 146px;
    display: flex; gap: 36px;
  }
  .detail-group { flex: 1; }
  .detail-title {
    font-size: 12px; font-weight: 700; letter-spacing: 2px;
    color: var(--orange); padding-bottom: 6px; margin-bottom: 8px;
    border-bottom: 1px solid #5a5a5a;
  }
  .detail-list { list-style: none; font-size: 12.5px; line-height: 1.55; color: var(--muted); }
  .detail-list li::before {
    content: ""; display: inline-block; width: 5px; height: 5px;
    background: var(--orange); margin: 0 8px 2px 0;
  }
</style>
</head>
<body>
<main class="stage">

  <section class="card card-front" aria-label="Business card front">
    <div class="name-band">
      <div class="person-name">OWEN HARTLEY</div>
      <div class="person-role">General Manager</div>
    </div>

    <div class="contact-panel">
      <div class="contact-row divided">
        <svg class="contact-icon" viewBox="0 0 16 16" aria-hidden="true"><path d="M1 4h14v9H1z M1 4l7 5 7-5" fill="none" stroke="#f1f1f1" stroke-width="1.6"/></svg>
        <div>Email: larkvale@mailbox.com<br>WEB: www.larkvalereview.com</div>
      </div>
      <div class="contact-row">
        <svg class="contact-icon" viewBox="0 0 16 16" aria-hidden="true"><rect x="4" y="1" width="8" height="14" rx="1.5" fill="none" stroke="#f1f1f1" stroke-width="1.6"/><circle cx="8" cy="12" r="1"/></svg>
        <div>Cell: +0961 52-80-14<br>Tel: 321 654 9870 2</div>
      </div>
      <div class="contact-row">
        <svg class="contact-icon" viewBox="0 0 16 16" aria-hidden="true"><path d="M8 1L1 8h2v7h4v-4h2v4h4V8h2z"/></svg>
        <div>Address Line 1<br>Address Line 2</div>
      </div>
    </div>

    <div class="brand">
      <span class="brand-mark" aria-hidden="true"></span>
      <span>Larkvale<br>Dwelling Review</span>
    </div>

    <div class="web-footer">WWW.LARKVALEREVIEW.COM</div>
    <div class="accent-band"></div>
    <div class="accent-base"></div>
  </section>

  <section class="card card-back" aria-label="Business card back">
    <div class="brand-plate">
      <div class="brand">
        <span class="brand-mark" aria-hidden="true"></span>
        <span>Larkvale Dwelling Review</span>
      </div>
    </div>

    <div class="back-details">
      <div class="detail-group">
        <div class="detail-title">SERVICES</div>
        <ul class="detail-list">
          <li>Residential Appraisals</li>
          <li>Home Inspection</li>
          <li>Pest Inspection</li>
          <li>Radon Gas Measurement</li>
        </ul>
      </div>
      <div class="detail-group">
        <div class="detail-title">QUALIFICATIONS</div>
        <ul class="detail-list">
          <li>State Certified Appraiser</li>
          <li>DRUMI Certified Inspector</li>
          <li>18 Years in Business</li>
          <li>Springfield, MO</li>
        </ul>
      </div>
    </div>
  </section>

</main>
</body>
</html>
```